Q-Rolls Business Card

We are a modern retail clothing store. Established in 1994. I need a presentable card that will amaze vendors when given to them.

Front: Logo in middle
Info Side:

Name: Tomas Velder
Cell: 630-812-4463
Work: 630-917-3384 EXT. 417
Email: Tomas@q-rolls-example.com
Website: www.Q-rolls-example.com

Industry/Entity Type

Business

```html
<!DOCTYPE html>
<html lang="en">
<head>
<meta charset="utf-8">
<title>Q-Rolls Business Card</title>
<link rel="stylesheet" href="https://fonts.googleapis.com/css2?family=Saira:wght@500;600&display=swap">
<style>
  :root {
    --backdrop: #ffffff;
    --paper: #e4e3e1;
    --paper-edge: #d2d0cd;
    --panel: #050505;
    --panel-text: #c9c9c9;
    --emboss-text: #c2c1bf;
    --ink: #111111;
    --edge-accent: #d9663c;
  }
  * { margin: 0; padding: 0; box-sizing: border-box; }
  html, body {
    width: 1200px;
    height: 1000px;
    overflow: hidden;
    background: var(--backdrop);
    font-family: "Saira", "Arial Narrow", sans-serif;
  }
  .canvas {
    position: relative;
    width: 1200px;
    height: 1000px;
  }
  .card {
    position: absolute;
    left: 250px;
    width: 700px;
    height: 400px;
    background: var(--paper);
    border-bottom: 6px solid var(--edge-accent);
    box-shadow: 0 10px 28px rgba(0,0,0,0.18);
  }
  .card--front { top: 60px; }
  .card--info { top: 530px; }

  .logo-panel {
    position: absolute;
    left: 175px;
    top: 60px;
    width: 350px;
    height: 190px;
    background: var(--panel);
    display: flex;
    align-items: center;
    justify-content: center;
  }
  .brand-name {
    font-weight: 600;
    font-size: 64px;
    letter-spacing: 1px;
    line-height: 1;
  }
  .logo-panel .brand-name { color: var(--panel-text); }

  .brand-emboss {
    position: absolute;
    left: 0;
    right: 0;
    top: 110px;
    text-align: center;
  }
  .brand-emboss .brand-name { color: var(--emboss-text); }

  .contact {
    position: absolute;
    list-style: none;
    color: var(--ink);
    font-weight: 500;
    font-size: 19px;
    line-height: 1.12;
  }
  .card--front .contact { left: 175px; top: 272px; }
  .card--info .contact { right: 30px; bottom: 30px; }
</style>
</head>
<body>
<main class="canvas">
  <section class="card card--front" aria-label="Card front">
    <div class="logo-panel">
      <span class="brand-name">Q-Rolls</span>
    </div>
    <ul class="contact">
      <li>Name: Tomas Velder</li>
      <li>Cell: 630-812-4463</li>
      <li>Work: 630-917-3384 EXT. 417</li>
      <li>Email: Tomas@q-rolls-example.com</li>
      <li>Website: www.Q-rolls-example.com</li>
    </ul>
  </section>

  <section class="card card--info" aria-label="Card info side">
    <div class="brand-emboss">
      <span class="brand-name">Q-Rolls</span>
    </div>
    <ul class="contact">
      <li>Name: Tomas Velder</li>
      <li>Cell: 630-812-4463</li>
      <li>Work: 630-917-3384 EXT. 417</li>
      <li>Email: Tomas@q-rolls-example.com</li>
      <li>Website: www.Q-rolls-example.com</li>
    </ul>
  </section>
</main>
</body>
</html>
```